" Somos um sistema que faz a gestão financeira de serviços automotivos como estética automotiva e lava-rápido. A operação acontece no smartphone, tablet ou PDV e a gestão através do site administrativos. São 2 módulos integrados. A cobrança é mensal, semestral e anual. Nosso site é www.velotrix.com.br "

```html
<!DOCTYPE html>
<html lang="pt-BR">
<head>
<meta charset="utf-8">
<title>Velotrix — Folder tri-fold</title>
<link rel="stylesheet" href="https://fonts.googleapis.com/css2?family=Montserrat:ital,wght@0,400;0,600;0,700;0,800;1,600;1,800&display=swap">
<style>
:root{
  --bg:#8a8a8a;
  --navy:#172b5c;
  --navy-dark:#10214a;
  --green:#1fb35a;
  --green-light:#34d06f;
  --white:#ffffff;
  --ink:#1d2a4a;
  --muted:#c9d3ea;
}
*{box-sizing:border-box;margin:0;padding:0}
html,body{width:1200px;height:1200px;overflow:hidden}
body{background:var(--bg);font-family:"Montserrat",sans-serif;position:relative}
.panel{position:absolute;top:300px;width:270px;height:600px;overflow:hidden}
.cover{left:45px;background:var(--white)}
.spread{position:absolute;left:345px;top:300px;width:810px;height:600px;box-shadow:0 10px 30px rgba(0,0,0,.25)}
.spread .panel{top:0}
.features-a{left:0;background:var(--navy)}
.features-b{left:270px;background:var(--navy);border-left:1px solid rgba(255,255,255,.08)}
.operation{left:540px;background:var(--white)}
.cover{box-shadow:0 10px 30px rgba(0,0,0,.25)}

/* cover */
.brand{display:flex;align-items:center;gap:10px;padding:40px 24px 0}
.brand-square{width:28px;height:28px;background:var(--green);border-radius:4px}
.brand-name{font-weight:800;font-size:26px;color:var(--navy)}
.cover-title{position:absolute;left:24px;right:24px;top:330px;font-size:20px;font-weight:600;color:var(--navy);line-height:1.2}
.cover-title b{font-weight:800;color:var(--green);display:block}
.cover-sub{position:absolute;left:24px;right:24px;top:400px;font-size:12px;color:var(--ink);line-height:1.45}
.cover-band{position:absolute;left:0;bottom:0;width:270px;height:110px}
.cover-site{position:absolute;left:0;right:0;bottom:22px;text-align:center;color:var(--white);font-weight:700;font-size:13px}

/* features */
.features-head{padding:22px 18px 0;color:var(--white);font-weight:800;font-size:13px;line-height:1.25;text-transform:uppercase}
.features-head::before{content:"";display:block;width:30px;height:4px;background:var(--green);margin-bottom:8px}
.feature-list{list-style:none;padding:14px 16px 0}
.features-b .feature-list{padding-top:26px}
.feature{display:flex;gap:12px;align-items:flex-start;margin-bottom:15px}
.features-b .feature{margin-bottom:22px}
.feature-icon{flex:0 0 40px;height:40px}
.feature-title{font-size:9.5px;font-weight:800;color:var(--green-light);text-transform:uppercase;line-height:1.2;margin-bottom:3px}
.feature-text{font-size:9px;color:var(--muted);line-height:1.35}

/* operation */
.op-head{padding:26px 18px 0 60px;text-align:right;color:var(--navy);font-size:17px;font-weight:600;font-style:italic;line-height:1.2}
.op-head b{color:var(--green);font-weight:800}
.op-list{list-style:none;padding:18px 16px 0}
.op-item{display:flex;gap:12px;align-items:flex-start;margin-bottom:14px}
.op-icon{flex:0 0 34px;height:34px}
.op-text{font-size:9px;color:var(--ink);line-height:1.35}
.op-text b{color:var(--navy);font-weight:800}
.plans{position:absolute;left:0;bottom:0;width:270px;height:210px}
.plans-bg{position:absolute;inset:0}
.plans-head{position:absolute;right:18px;top:40px;text-align:right;color:var(--white);line-height:1.05}
.plans-head strong{display:block;font-size:22px;font-weight:800}
.plans-head span{font-size:17px;font-style:italic;font-weight:600}
.plan-row{position:absolute;left:12px;right:12px;bottom:22px;display:flex;gap:8px}
.plan{flex:1;text-align:center}
.plan-name{background:var(--white);color:var(--navy);font-size:8.5px;font-weight:800;padding:4px 0;border-radius:3px;text-transform:uppercase}
.plan-price{color:var(--white);font-weight:800;font-size:32px;line-height:1.1;margin-top:6px}
.plan-price small{font-size:9px;font-weight:700;vertical-align:top;margin-right:2px}
</style>
</head>
<body>

<section class="panel cover">
  <div class="brand"><span class="brand-square"></span><span class="brand-name">Velotrix</span></div>
  <h2 class="cover-title">Sistema de gestão <b>automotiva</b></h2>
  <p class="cover-sub">Mais tempo para você e seu cliente agradecido pelo serviço.</p>
  <svg class="cover-band" viewBox="0 0 270 110" aria-hidden="true">
    <path d="M0 30 Q135 -10 270 30 V110 H0Z" fill="var(--green)"/>
    <path d="M0 50 Q135 15 270 50 V110 H0Z" fill="var(--navy)"/>
  </svg>
  <p class="cover-site">www.velotrix.com.br</p>
</section>

<div class="spread">
  <section class="panel features-a">
    <h2 class="features-head">Funcionalidades importante que resolvem seus problemas operacionais e administrativos</h2>
    <ul class="feature-list">
      <li class="feature">
        <svg class="feature-icon" viewBox="0 0 40 40" aria-hidden="true"><rect x="5" y="10" width="30" height="20" rx="2" fill="none" stroke="var(--green)" stroke-width="2.5"/><circle cx="20" cy="20" r="5" fill="var(--green)"/></svg>
        <div><h3 class="feature-title">Fluxo de caixa completo</h3><p class="feature-text">Contas a pagar e a receber. Uma gestão financeira completa.</p></div>
      </li>
      <li class="feature">
        <svg class="feature-icon" viewBox="0 0 40 40" aria-hidden="true"><path d="M9 4h16l7 7v25H9Z" fill="none" stroke="var(--green)" stroke-width="2.5"/><path d="M14 20h13M14 26h13" stroke="var(--green)" stroke-width="2.5"/></svg>
        <div><h3 class="feature-title">Emissão de NFS-e</h3><p class="feature-text">Emita NFS-e em serviços direto para seu cliente (opcional).</p></div>
      </li>
      <li class="feature">
        <svg class="feature-icon" viewBox="0 0 40 40" aria-hidden="true"><circle cx="20" cy="13" r="7" fill="var(--green)"/><path d="M6 36c0-9 6-13 14-13s14 4 14 13Z" fill="var(--green)"/></svg>
        <div><h3 class="feature-title">Gestão dos clientes pós pago</h3><p class="feature-text">Gerencie aqueles clientes que pagam depois sem se atrapalhar nos relatórios.</p></div>
      </li>
      <li class="feature">
        <svg class="feature-icon" viewBox="0 0 40 40" aria-hidden="true"><circle cx="20" cy="20" r="14" fill="none" stroke="var(--green)" stroke-width="2.5"/><path d="M20 11v18M15 15h8a3 3 0 0 1 0 6h-6a3 3 0 0 0 0 6h8" fill="none" stroke="var(--green)" stroke-width="2.5"/></svg>
        <div><h3 class="feature-title">Gestão dos comissionamentos</h3><p class="feature-text">Automatize o controle de comissionamento de quem faz a empresa crescer.</p></div>
      </li>
      <li class="feature">
        <svg class="feature-icon" viewBox="0 0 40 40" aria-hidden="true"><rect x="8" y="5" width="24" height="31" rx="2" fill="none" stroke="var(--green)" stroke-width="2.5"/><path d="M13 15l3 3 6-6M13 25h14" fill="none" stroke="var(--green)" stroke-width="2.5"/></svg>
        <div><h3 class="feature-title">Cadastro e relatório dos clientes</h3><p class="feature-text">Veja todos seus clientes e exporte para fazer uma ação de marketing se quiser.</p></div>
      </li>
      <li class="feature">
        <svg class="feature-icon" viewBox="0 0 40 40" aria-hidden="true"><rect x="8" y="5" width="24" height="31" rx="2" fill="var(--green)"/><path d="M13 14h14M13 20h14M13 26h9" stroke="var(--navy)" stroke-width="2.5"/></svg>
        <div><h3 class="feature-title">Relatórios</h3><p class="feature-text">Veja relatórios resumidos ou detalhados.</p></div>
      </li>
    </ul>
  </section>

  <section class="panel features-b">
    <ul class="feature-list">
      <li class="feature">
        <svg class="feature-icon" viewBox="0 0 40 40" aria-hidden="true"><rect x="5" y="11" width="30" height="22" rx="3" fill="var(--green)"/><rect x="14" y="7" width="12" height="6" fill="var(--green)"/><circle cx="20" cy="22" r="6" fill="var(--navy)"/></svg>
        <div><h3 class="feature-title">Registro com 05 fotos</h3><p class="feature-text">Aumente a confiabilidade com fotos do veículo no atendimento.</p></div>
      </li>
      <li class="feature">
        <svg class="feature-icon" viewBox="0 0 40 40" aria-hidden="true"><circle cx="20" cy="20" r="15" fill="var(--green)"/></svg>
        <div><h3 class="feature-title">Envio de ChatLink</h3><p class="feature-text">Envie alerta ao seu cliente avisando que o veículo está pronto.</p></div>
      </li>
      <li class="feature">
        <svg class="feature-icon" viewBox="0 0 40 40" aria-hidden="true"><rect x="6" y="14" width="28" height="20" rx="2" fill="none" stroke="var(--green)" stroke-width="2.5"/><path d="M12 14V9h16v5" fill="none" stroke="var(--green)" stroke-width="2.5"/></svg>
        <div><h3 class="feature-title">Acesso sem fundo de caixa</h3><p class="feature-text">Opere sem fundo de caixa e registre os pagamentos com precisão.</p></div>
      </li>
      <li class="feature">
        <svg class="feature-icon" viewBox="0 0 40 40" aria-hidden="true"><rect x="5" y="7" width="30" height="22" rx="2" fill="none" stroke="var(--green)" stroke-width="2.5"/><path d="M10 24l7-7 5 4 8-9" fill="none" stroke="var(--green)" stroke-width="2.5"/><path d="M15 35h10M20 29v6" stroke="var(--green)" stroke-width="2.5"/></svg>
        <div><h3 class="feature-title">Marketing de pós venda</h3><p class="feature-text">Aumente a recorrência facilitando o retorno do seu cliente.</p></div>
      </li>
      <li class="feature">
        <svg class="feature-icon" viewBox="0 0 40 40" aria-hidden="true"><rect x="5" y="7" width="30" height="22" rx="2" fill="none" stroke="var(--green)" stroke-width="2.5"/><path d="M14 13h12l-2 9H16Z" fill="var(--green)"/><path d="M15 35h10M20 29v6" stroke="var(--green)" stroke-width="2.5"/></svg>
        <div><h3 class="feature-title">Venda de produto</h3><p class="feature-text">Incremente sua receita com venda de produtos.</p></div>
      </li>
      <li class="feature">
        <svg class="feature-icon" viewBox="0 0 40 40" aria-hidden="true"><path d="M6 18L18 6h14v14L20 32Z" fill="none" stroke="var(--green)" stroke-width="2.5"/><circle cx="26" cy="12" r="2.5" fill="var(--green)"/></svg>
        <div><h3 class="feature-title">Vendas de pacotes de serviços</h3><p class="feature-text">Faça promoções e gere receita antecipada.</p></div>
      </li>
    </ul>
  </section>

  <section class="panel operation">
    <h2 class="op-head">Seu negócio, sua <b>escolha como operar.</b></h2>
    <ul class="op-list">
      <li class="op-item">
        <svg class="op-icon" viewBox="0 0 34 34" aria-hidden="true"><rect x="3" y="5" width="28" height="18" rx="2" fill="none" stroke="var(--navy)" stroke-width="2.5"/><path d="M11 30h12M17 23v7" stroke="var(--navy)" stroke-width="2.5"/></svg>
        <p class="op-text"><b>Opera pelo Computador:</b> sistema para o PDV ou balcão com tela de atendimento.</p>
      </li>
      <li class="op-item">
        <svg class="op-icon" viewBox="0 0 34 34" aria-hidden="true"><rect x="9" y="3" width="16" height="28" rx="3" fill="none" stroke="var(--navy)" stroke-width="2.5"/><circle cx="17" cy="26" r="1.6" fill="var(--navy)"/></svg>
        <p class="op-text"><b>Smartphone ou Tablet:</b> atenda seu cliente no pátio e registre tudo na hora.</p>
      </li>
      <li class="op-item">
        <svg class="op-icon" viewBox="0 0 34 34" aria-hidden="true"><rect x="4" y="4" width="10" height="10" fill="none" stroke="var(--navy)" stroke-width="2.5"/><rect x="20" y="4" width="10" height="10" fill="none" stroke="var(--navy)" stroke-width="2.5"/><rect x="4" y="20" width="10" height="10" fill="none" stroke="var(--navy)" stroke-width="2.5"/><rect x="21" y="21" width="8" height="8" fill="var(--navy)"/></svg>
        <p class="op-text"><b>O Código QR:</b> seu cliente acompanha o serviço pelo celular.</p>
      </li>
      <li class="op-item">
        <svg class="op-icon" viewBox="0 0 34 34" aria-hidden="true"><rect x="4" y="12" width="26" height="13" rx="2" fill="none" stroke="var(--navy)" stroke-width="2.5"/><path d="M10 12V4h14v8M10 21h14v9H10Z" fill="none" stroke="var(--navy)" stroke-width="2.5"/></svg>
        <p class="op-text"><b>A Impressora Portátil:</b> imprima comprovantes em qualquer lugar, <b>menos papel.</b></p>
      </li>
    </ul>
    <div class="plans">
      <svg class="plans-bg" viewBox="0 0 270 210" preserveAspectRatio="none" aria-hidden="true">
        <path d="M0 40 Q150 -15 270 12 V210 H0Z" fill="var(--green)"/>
      </svg>
      <div class="plans-head"><strong>GOSTOU?</strong><span>Planos acessíveis!</span></div>
      <div class="plan-row">
        <div class="plan"><div class="plan-name">Mensal</div><div class="plan-price"><small>R$</small>69</div></div>
        <div class="plan"><div class="plan-name">Semestral</div><div class="plan-price"><small>R$</small>59</div></div>
        <div class="plan"><div class="plan-name">Anual</div><div class="plan-price"><small>R$</small>49</div></div>
      </div>
    </div>
  </section>
</div>

</body>
</html>
```